Leaf Orrin medical cannibis cultivation company

tag - Orrin rise
Leaf Orrin medical cannabis cultivation - logo is selected- can we please see bold examples with our selection. We are mainly dealing with medical companies and professionals. We would like to be stand out in the crowd with our designs. Welcome any and all attempts. Thanks

Target Market(s)

Medical and Professional

Industry/Entity Type

Medical And Science

Font styles to use
Sans Serif

Colors

Designer to choose colors to be used in the design.

Requirements
Must have
• Bright colour and be bold- Love the teal and magenta that is currently on the dark background design.
Nice to have
• shading and the 3D affect- The shadowed appearance.
Should not have
• Anything related to illegal activity or un professional manners

```html
<!DOCTYPE html>
<html lang="en">
<head>
<meta charset="utf-8">
<title>Leaf Orrin Stationery</title>
<link href="https://fonts.googleapis.com/css2?family=Montserrat:wght@400;500;600&family=Open+Sans:wght@400&display=swap" rel="stylesheet">
<style>
:root{
  --teal:#12847c;
  --magenta:#9b4a9c;
  --grey:#6f7274;
  --ink:#333;
  --paper:#fff;
  --dark:#1c1c1d;
}
*{margin:0;padding:0;box-sizing:border-box}
html,body{width:1200px;height:804px;overflow:hidden;background:#fff}
body{position:relative;font-family:'Montserrat',sans-serif;color:var(--ink)}
.sheet{position:absolute;background:var(--paper);box-shadow:2px 3px 6px rgba(0,0,0,.35);overflow:hidden}
.mark-ring{position:absolute;border:3px solid #8a8d90;border-radius:50%}
.wordmark{position:absolute;left:0;right:0;text-align:center;font-family:'Montserrat',sans-serif;font-weight:600;color:var(--teal);text-transform:uppercase;letter-spacing:.02em;line-height:1}
.tagline{position:absolute;left:0;right:0;text-align:center;font-family:'Montserrat',sans-serif;color:var(--grey);text-transform:uppercase;letter-spacing:.15em;line-height:1}
.tagline span{display:inline-block;padding:0 4px;position:relative}
.tagline span::before,.tagline span::after{content:"";position:absolute;top:50%;width:34px;border-top:1px solid var(--grey)}
.tagline span::before{right:100%}.tagline span::after{left:100%}
.icon{width:11px;height:11px;fill:none;stroke:var(--magenta);stroke-width:1.6}
.contact-row{position:absolute;display:flex;align-items:flex-end}
.contact{display:flex;flex-direction:column;align-items:center;justify-content:flex-end;font-size:11px;color:#222;white-space:nowrap;padding:0 6px;height:42px}
.contact .icon{margin-bottom:6px}
.contact.address{align-items:flex-start;text-align:left;line-height:1.2}
.contact.address .icon{align-self:center;margin-bottom:3px}
.divider{width:1px;height:42px;background:#333}
.band{position:absolute;display:flex;left:0;right:0}
.band .seg{height:100%}
.band .disc{position:absolute;top:50%;border-radius:50%;background:#fff;border:2px solid #8a8d90;transform:translate(-50%,-50%)}

/* letterhead */
.letterhead{left:49px;top:42px;width:552px;height:712px}
.letter{position:absolute;left:42px;top:240px;width:469px;font-family:'Open Sans',sans-serif;font-size:8.8px;line-height:10.8px;color:#222}
.letter p{margin-bottom:10.8px;text-align:justify}
.letter .sign{text-align:left;margin-bottom:10.8px}

/* business cards */
.card-front{left:622px;top:44px;width:279px;height:158px}
.card-front .name-panel{position:absolute;left:0;top:57px;width:279px;height:68px;background:var(--magenta)}
.card-front .teal-tab{position:absolute;left:230px;top:57px;width:49px;height:62px;background:var(--teal)}
.card-front .holder{position:absolute;left:16px;top:64px;color:#fff}
.holder .person{font-size:12px;font-weight:500}
.holder .role{font-size:6.5px;margin-top:1px}
.holder .rule{width:6px;border-top:1px solid #fff;margin:4px 0 4px}
.holder li{list-style:none;font-size:6.6px;line-height:9.5px;display:flex;align-items:center;gap:3px}
.holder li::before{content:"";width:4px;height:4px;border-radius:50%;border:1px solid #fff}
.card-front .addr{position:absolute;left:16px;top:132px;font-size:6.8px;color:#222;display:flex;align-items:center;gap:3px}
.card-front .addr .icon{width:7px;height:7px;stroke:var(--teal)}
.card-back{left:908px;top:44px;width:278px;height:158px;background:linear-gradient(120deg,#2a2a2b,#141415 70%,#2a2a2b)}

/* envelope */
.envelope{left:621px;top:225px;width:565px;height:250px}
.envelope-back{left:622px;top:501px;width:565px;height:250px}
.flap{position:absolute;left:0;top:0}
</style>
</head>
<body>
<svg width="0" height="0" style="position:absolute" aria-hidden="true">
  <symbol id="i-phone" viewBox="0 0 24 24"><circle cx="12" cy="12" r="10.5"/><path d="M8.5 7.5c.5-.6 1.4-.6 1.8 0l.9 1.5c.3.5.2 1.1-.2 1.4l-.6.5c.6 1.4 1.6 2.4 3 3l.5-.6c.3-.4.9-.5 1.4-.2l1.5.9c.6.4.6 1.3 0 1.8-1.2 1.1-3 1.1-4.8-.3-1.6-1.2-2.9-2.7-3.6-4.3-.7-1.6-.6-2.9.1-3.7z"/></symbol>
  <symbol id="i-mail" viewBox="0 0 24 24"><circle cx="12" cy="12" r="10.5"/><rect x="6.5" y="8" width="11" height="8" rx="1"/><path d="M6.5 8.5l5.5 4 5.5-4"/></symbol>
  <symbol id="i-web" viewBox="0 0 24 24"><circle cx="12" cy="12" r="10.5"/><circle cx="12" cy="12" r="6"/><path d="M6 12h12M12 6c-2 2-2 10 0 12M12 6c2 2 2 10 0 12"/></symbol>
  <symbol id="i-pin" viewBox="0 0 24 24"><path d="M12 22s-7-7-7-12a7 7 0 0 1 14 0c0 5-7 12-7 12z"/><circle cx="12" cy="10" r="2.5"/></symbol>
</svg>

<!-- Letterhead -->
<section class="sheet letterhead">
  <div class="mark-ring" style="left:226px;top:24px;width:100px;height:100px"></div>
  <div class="wordmark" style="top:127px;font-size:30px">Leaf Orrin</div>
  <div class="tagline" style="top:154px;font-size:11px"><span>Orrin Rise</span></div>

  <div class="letter">
    <p class="sign">Dear Mr. Hale,</p>
    <p>Lorem ipsum dolor sit amet, consectetuer adipiscing elit, sed diam nonummy nibh euismod tincidunt ut laoreet dolore magna aliquam erat volutpat. Ut wisi enim ad minim veniam, quis nostrud exerci tation ullamcorper suscipit lobortis nisl ut aliquip ex ea commodo consequat. Duis autem vel eum iriure dolor in hendrerit in vulputate velit esse molestie consequat,</p>
    <p>Lorem ipsum dolor sit amet, consectetuer adipiscing elit, sed diam nonummy nibh euismod tincidunt ut laoreet dolore magna aliquam erat volutpat. Ut wisi enim ad minim veniam, quis nostrud exerci tation ullamcorper suscipit lobortis nisl ut aliquip ex ea commodo consequat. Duis autem vel eum iriure dolor in hendrerit in vulputate velit esse molestie consequat, vel illum dolore eu feugiat nulla facilisis at vero eros et accumsan et iusto odio dignissim qui blandit praesent luptatum zzril delenit augue duis dolore te feugait nulla facilisi. Nam liber tempor cum soluta nobis eleifend option congue nihil imperdiet doming id quod mazim placerat facer possim assum.,</p>
    <p>Lorem ipsum dolor sit amet, consectetuer adipiscing elit, sed diam nonummy nibh euismod tincidunt ut laoreet dolore magna aliquam erat volutpat. Ut wisi enim ad minim veniam, quis nostrud exerci tation ullamcorper suscipit lobortis nisl ut aliquip ex ea commodo consequat. Duis autem vel eum iriure dolor in hendrerit in vulputate velit esse molestie consequat,</p>
    <p class="sign">Sincerely,</p>
    <p class="sign">Ada Wren<br>Sales Manager</p>
  </div>

  <div class="contact-row" style="left:14px;top:634px">
    <div class="contact"><svg class="icon"><use href="#i-phone"/></svg>+0 123 456 789</div>
    <div class="divider"></div>
    <div class="contact"><svg class="icon"><use href="#i-mail"/></svg>info@yourmail.com</div>
    <div class="divider"></div>
    <div class="contact"><svg class="icon"><use href="#i-web"/></svg>www.yourcompany.com</div>
    <div class="divider"></div>
    <div class="contact address"><svg class="icon"><use href="#i-pin"/></svg>Your address, Suit # 000,<br>Dummy Street City, State</div>
  </div>

  <div class="band" style="top:686px;height:24px">
    <div class="seg" style="width:276px;background:var(--magenta)"></div>
    <div class="seg" style="flex:1;background:var(--teal)"></div>
    <div class="disc" style="left:276px;width:26px;height:26px"></div>
  </div>
</section>

<!-- Business card front -->
<section class="sheet card-front">
  <div class="wordmark" style="left:16px;right:auto;top:14px;font-size:21px">Leaf Orrin</div>
  <div class="tagline" style="left:16px;right:auto;width:131px;top:37px;font-size:8px"><span>Orrin Rise</span></div>
  <div class="name-panel"></div>
  <div class="teal-tab"></div>
  <div class="mark-ring" style="left:182px;top:56px;width:76px;height:76px;background:#fff;border-width:2px"></div>
  <div class="holder">
    <div class="person">Person’s Name</div>
    <div class="role">Designation</div>
    <div class="rule"></div>
    <ul>
      <li>+0 123 456 789</li>
      <li>info@yourmail.com</li>
      <li>www.yourcompany.com</li>
    </ul>
  </div>
  <div class="addr"><svg class="icon"><use href="#i-pin"/></svg>Your address, Suit # 000, Dummy Street, City, State,</div>
</section>

<!-- Business card back -->
<section class="sheet card-back">
  <div class="mark-ring" style="left:100px;top:22px;width:76px;height:76px;border-color:#7d8083"></div>
  <div class="wordmark" style="top:101px;font-size:24px">Leaf Orrin</div>
  <div class="tagline" style="top:124px;font-size:9px;color:#9a9c9e"><span>Orrin Rise</span></div>
</section>

<!-- Envelope front -->
<section class="sheet envelope">
  <div class="mark-ring" style="left:243px;top:12px;width:78px;height:78px"></div>
  <div class="wordmark" style="top:92px;font-size:24px">Leaf Orrin</div>
  <div class="tagline" style="top:115px;font-size:9.5px"><span>Orrin Rise</span></div>
  <div class="contact-row" style="left:32px;top:170px">
    <div class="contact"><svg class="icon"><use href="#i-phone"/></svg>+0 123 456 789</div>
    <div class="divider"></div>
    <div class="contact"><svg class="icon"><use href="#i-mail"/></svg>info@yourmail.com</div>
    <div class="divider"></div>
    <div class="contact"><svg class="icon"><use href="#i-web"/></svg>www.yourcompany.com</div>
    <div class="divider"></div>
    <div class="contact address"><svg class="icon"><use href="#i-pin"/></svg>Your address, Suit # 000,<br>Dummy Street City, State</div>
  </div>
  <div class="band" style="top:225px;height:24px">
    <div class="seg" style="width:283px;background:var(--magenta)"></div>
    <div class="seg" style="flex:1;background:var(--teal)"></div>
    <div class="disc" style="left:283px;width:26px;height:26px"></div>
  </div>
</section>

<!-- Envelope back -->
<section class="sheet envelope-back">
  <svg class="flap" width="565" height="74" viewBox="0 0 565 74" aria-hidden="true">
    <path d="M0 0H565L538 58Q531 73 514 73H51Q34 73 27 58Z" fill="var(--dark)"/>
  </svg>
  <div class="mark-ring" style="left:264px;top:13px;width:38px;height:38px;border-width:2px;border-color:#7d8083"></div>
  <div class="wordmark" style="top:53px;font-size:12px">Leaf Orrin</div>
  <div class="band" style="top:226px;height:24px">
    <div class="seg" style="width:282px;background:var(--teal)"></div>
    <div class="seg" style="flex:1;background:var(--magenta)"></div>
    <div class="disc" style="left:282px;width:26px;height:26px"></div>
  </div>
</section>
</body>
</html>
```